Wordpress Contest Brief I would like a WordPress theme designed

Industry / Entity Type

Financial consultancy / advisers

Current site is: http://www.quorvel-group.com

Looking for a complete overhaul of this site, we are after a clean modern look. Will require the ability to easily add, update and remove content, hence the WordPress design.
Example:
Add case studies
Industry documentation (downloadable brochures / flyers and such)

What we like from our current site is the colour the fonts and the logo (the city of London) we would like to have other city outlines (NYC and Tokyo, Hong Kong, Singapore).

The site will be used by our potential clients to get in contact and re-view the case studies, if possible would like to have a client login area where they can download our documents like NDA’s etc and T&C’s.

Task Outline

Create a Web Design (Coded - Design and coding required)
Designer must provide full implementation/coding depending on the platform chosen by the client (i.e. WordPress theme, HTML/CSS, bootstrap etc.)

Task Description

I need a full website built that must work on desktop and mobile. I can provide the London city skyline and the font file, which we have used. Some stock industrial photos will be required.

Requirements:

*Splash page
*What We Do
*How We do it
*Who Are We? To have the same information and links as the current site
*Why use us?
*Clients: To have the same information and links as the current site
*Partners: To have the same information and links as the current site
*Contact:

Target Market(s)

Financial institutions trading Equities, Futures, Options, Forex and Fixed Income.
Regulators, Exchanges, ECN’s
Buy side firms and Sell side firms

Industry/Entity Type

Financial

Coding

Coded - Design and coding required

Number of Pages Required

5+ page

Font styles to use
Sans Serif

Colors
f04a50

Requirements
Must have
• Splash page
• What We Do
• How We do it
• Who Are We? To have the same information and links as the current site
• Why use us?
• Clients: To have the same information and links as the current site
• Partners: To have the same information and links as the current site
• Contact:

```html
<!DOCTYPE html>
<html lang="en">
<head>
<meta charset="utf-8">
<title>Quorvel Technology Advisers</title>
<link rel="stylesheet" href="https://fonts.googleapis.com/css2?family=Alegreya+Sans:wght@400;500;700&display=swap">
<style>
:root{
  --red:#f04a50;
  --ink:#333333;
  --muted:#666666;
  --grey-bg:#f2f2f2;
  --white:#ffffff;
  --footer:#232323;
  --footer-deep:#1a1a1a;
  --footer-text:#d8d8d8;
}
*{box-sizing:border-box;margin:0;padding:0}
html,body{width:1200px;height:3837px;overflow:hidden}
body{font-family:"Alegreya Sans",Arial,sans-serif;color:var(--ink);font-size:14px;line-height:24px;background:var(--white)}
.wrap{width:960px;margin:0 auto;position:relative;height:100%}
section,header,footer{position:relative;overflow:hidden}
h2.section-title{color:var(--red);font-weight:500;font-size:25px;text-align:center}
.circle-link{display:inline-block;width:20px;height:20px;border:1.5px solid var(--red);border-radius:50%;position:relative;flex:none}
.circle-link::after{content:"";position:absolute;left:5px;top:4px;width:5px;height:5px;border-right:1.5px solid var(--red);border-bottom:1.5px solid var(--red);transform:rotate(45deg)}

/* header */
.site-header{height:100px;background:var(--white)}
.brand{position:absolute;left:40px;top:30px;display:flex;align-items:center;gap:10px;font-size:17px;font-weight:500;letter-spacing:2px;color:var(--ink)}
.brand-mark{width:14px;height:14px;background:var(--ink)}
.topbar{position:absolute;right:0;top:12px;display:flex;gap:16px;font-size:13px;align-items:center}
.topbar .item{display:flex;align-items:center;gap:5px}
.main-nav{position:absolute;right:0;top:58px;display:flex;gap:20px;font-size:14px;font-weight:500;align-items:center}
.main-nav .active{color:var(--red)}

/* hero */
.hero{height:383px;background:linear-gradient(180deg,#7fa6cf 0%,#b9cbe0 35%,#8c8f94 60%,#5b5a58 100%)}
.hero-photo{position:absolute;inset:0}
.hero-band{position:absolute;left:180px;top:105px;width:786px;height:80px;background:rgba(240,74,80,.72);padding:10px 20px;color:var(--white)}
.hero-band .hero-title{font-size:26px;letter-spacing:3px;font-weight:500;line-height:30px;color:transparent;-webkit-text-stroke:1px var(--white)}
.hero-band p{font-size:14px;line-height:17px;font-weight:500}

/* welcome */
.welcome{height:322px;text-align:center}
.welcome h2{position:absolute;top:68px;width:100%}
.welcome p{position:absolute;top:120px;left:0;width:960px;font-size:14px;line-height:27px}

/* services */
.services{height:629px;background:var(--grey-bg)}
.services h2{position:absolute;top:68px;width:100%}
.service-grid{position:absolute;top:148px;left:0;width:960px;display:grid;grid-template-columns:repeat(3,320px);row-gap:52px}
.service{text-align:center;padding:0 30px}
.service svg{display:block;margin:0 auto 8px}
.service h3{color:var(--red);font-weight:500;font-size:16px;line-height:22px}
.service p{font-size:13px;line-height:22px;min-height:44px;margin-bottom:14px}

/* partners */
.partners{height:372px}
.side-intro{position:absolute;left:0;top:70px;width:190px}
.side-intro h2{color:var(--red);font-weight:500;font-size:19px;margin-bottom:26px}
.side-intro p{font-size:13px;line-height:22px}
.logo-name{font-size:19px;font-weight:700;color:var(--ink);display:flex;align-items:center;gap:8px;white-space:nowrap}
.logo-dot{width:12px;height:12px;border-radius:50%;background:var(--ink);flex:none}
.logo-sq{width:12px;height:12px;background:var(--ink);flex:none}
.partner-logos{position:absolute;left:250px;top:90px;width:710px;height:230px}
.partner-logos .logo-name{position:absolute}

/* team */
.team{height:550px;background:var(--grey-bg)}
.team h2{position:absolute;top:75px;width:100%}
.team-cards{position:absolute;top:150px;left:0;width:960px;display:flex;justify-content:space-between}
.member{width:196px;height:256px;background:var(--white);box-shadow:0 1px 6px rgba(0,0,0,.15);text-align:center;padding:14px 14px 0}
.member-photo{display:block;width:168px;height:160px;margin:0 auto 10px}
.member h3{color:var(--red);font-weight:500;font-size:15px;line-height:20px}
.member .role{font-size:12px;line-height:18px}
.member .profile{display:flex;align-items:center;justify-content:center;gap:8px;font-size:13px;margin-top:14px}

/* clients */
.clients{height:498px}
.clients .side-intro{top:52px;width:180px}
.client-logos{position:absolute;left:0;top:0;width:960px;height:498px}
.client-logos .logo-name{position:absolute}

/* case studies / about */
.info{height:539px;background:var(--grey-bg)}
.case-studies{position:absolute;left:0;top:72px;width:460px}
.case-studies h2{color:var(--red);font-weight:500;font-size:22px;line-height:28px;margin-bottom:32px}
.case-list{list-style:none}
.case-list li{display:flex;align-items:center;gap:18px;font-size:13px;height:52px}
.about{position:absolute;left:520px;top:72px;width:440px}
.about h2{color:var(--red);font-weight:500;font-size:22px;line-height:28px;margin-bottom:16px}
.about p{font-size:13px;line-height:24px}

/* footer */
.site-footer{height:337px;background:var(--footer);color:var(--footer-text)}
.footer-contact{position:absolute;left:0;top:34px;width:300px;font-size:13px;line-height:22px}
.footer-contact h4,.footer-privacy h4{color:var(--white);font-weight:500;font-size:16px;margin-bottom:22px}
.footer-contact .line{display:flex;align-items:center;gap:6px;margin-bottom:22px}
.footer-privacy{position:absolute;left:335px;top:34px;width:625px;font-size:12.5px;line-height:22px}
.footer-nav{height:44px;background:var(--footer-deep);display:flex;justify-content:center;align-items:center;gap:22px;font-size:12px;color:var(--white);border-top:1px solid #333}
.copyright{height:61px;background:var(--footer-deep);border-top:1px solid #2c2c2c;color:var(--footer-text);font-size:12px}
.copyright .wrap{display:flex;justify-content:space-between;align-items:center}
</style>
</head>
<body>

<header class="site-header">
  <div class="wrap">
    <div class="brand"><span class="brand-mark"></span>QUORVEL TECHNOLOGY ADVISERS</div>
    <div class="topbar">
      <span class="item"><svg width="12" height="12" viewBox="0 0 24 24"><path d="M6 2l4 5-2 3c1 3 3 5 6 6l3-2 5 4-3 4C10 22 2 14 2 5z" fill="#333"/></svg>+44(0)20 7946 0382</span>
      <span class="item"><svg width="13" height="10" viewBox="0 0 26 20"><rect x="1" y="1" width="24" height="18" fill="none" stroke="#333" stroke-width="2"/><path d="M1 1l12 10L25 1" fill="none" stroke="#333" stroke-width="2"/></svg>admin@quorvel-group.com</span>
      <span class="item">Social</span>
      <span class="item"><svg width="12" height="12" viewBox="0 0 24 24"><circle cx="12" cy="8" r="5" fill="#333"/><path d="M2 23c0-6 4-9 10-9s10 3 10 9z" fill="#333"/></svg>Clients</span>
      <span class="item">Partners</span>
      <span class="item">Login</span>
    </div>
    <nav class="main-nav">
      <span class="active">Home</span><span>What We Do</span><span>How We do it</span><span>Who Are We</span><span>Why use us?</span><span>Contact</span>
      <svg width="12" height="12" viewBox="0 0 24 24"><circle cx="10" cy="10" r="7" fill="none" stroke="#333" stroke-width="2.5"/><path d="M15 15l7 7" stroke="#333" stroke-width="2.5"/></svg>
    </nav>
  </div>
</header>

<section class="hero">
  <div class="hero-photo" role="img" aria-label="Glass office towers in a financial district seen from street level against a blue sky"></div>
  <div class="hero-band">
    <div class="hero-title">Quorvel Technology Advisers</div>
    <p>QTA is dedicated to seeing you choose the right technology strategy, ensuring<br>you maintain a competitive edge over your peers.</p>
  </div>
</section>

<section class="welcome">
  <div class="wrap">
    <h2 class="section-title">Welcome to Quorvel Technology Advisers</h2>
    <p>Since founding Quorvel Technology Advisers in 2014 we have dedicated ourselves to the provision of services. What differentiates us from other advisers or consultancies is a genuine motivation to see our clients succeed. Today's technology allows our clients to take their knowledge to the market in ways that previous generations could only dream of. That's why QTA is dedicated to seeing you choose the right technology strategy, ensuring you maintain a competitive edge over your peers.</p>
  </div>
</section>

<section class="services">
  <div class="wrap">
    <h2 class="section-title">What We Do</h2>
    <div class="service-grid">
      <div class="service">
        <svg width="28" height="28" viewBox="0 0 28 28"><rect x="4" y="4" width="20" height="14" fill="none" stroke="#333" stroke-width="2"/><path d="M14 18v6M9 24h10" stroke="#333" stroke-width="2"/></svg>
        <h3>Training</h3><p>Trading technology for compliance and non technical staff</p><span class="circle-link"></span>
      </div>
      <div class="service">
        <svg width="28" height="28" viewBox="0 0 28 28"><circle cx="14" cy="12" r="9" fill="none" stroke="#333" stroke-width="2"/><path d="M10 26l4-6 4 6" fill="none" stroke="#333" stroke-width="2"/><circle cx="14" cy="12" r="3" fill="#333"/></svg>
        <h3>Research</h3><p>Topical Papers white labelled and sponsored articles</p><span class="circle-link"></span>
      </div>
      <div class="service">
        <svg width="28" height="28" viewBox="0 0 28 28"><path d="M14 3l10 5v2H4V8z" fill="#333"/><path d="M7 11v10M12 11v10M16 11v10M21 11v10M4 24h20" stroke="#333" stroke-width="2"/></svg>
        <h3>MiFID II</h3><p>QTA can assist your technology, then provide solutions to solve potential issues.</p><span class="circle-link"></span>
      </div>
      <div class="service">
        <svg width="28" height="28" viewBox="0 0 28 28"><circle cx="14" cy="12" r="6" fill="none" stroke="#333" stroke-width="2"/><path d="M11 20h6M12 24h4M14 2v2M4 12H2M26 12h-2M6 5l1 1M22 5l-1 1" stroke="#333" stroke-width="2"/></svg>
        <h3>Advice</h3><p>Board level Advisory &amp; Program Management</p><span class="circle-link"></span>
      </div>
      <div class="service">
        <svg width="28" height="28" viewBox="0 0 28 28"><circle cx="11" cy="15" r="6" fill="none" stroke="#333" stroke-width="3" stroke-dasharray="3 2"/><circle cx="21" cy="7" r="4" fill="none" stroke="#333" stroke-width="2.5" stroke-dasharray="2 2"/></svg>
        <h3>Product Development</h3><p>Front – Office Trading Platforms &amp; Market Data Pit | At | Post Trade Risk</p><span class="circle-link"></span>
      </div>
      <div class="service">
        <svg width="28" height="28" viewBox="0 0 28 28"><circle cx="8" cy="8" r="3" fill="#333"/><circle cx="20" cy="8" r="3" fill="#333"/><circle cx="14" cy="12" r="3" fill="#333"/><path d="M3 20c0-4 3-6 5-6s5 2 5 6zM15 20c0-4 3-6 5-6s5 2 5 6zM8 25c0-5 3-7 6-7s6 2 6 7z" fill="#333"/></svg>
        <h3>Interim Management</h3><p>For funds, Brokers, Vendors &amp; IT Service providers</p><span class="circle-link"></span>
      </div>
    </div>
  </div>
</section>

<section class="partners">
  <div class="wrap">
    <div class="side-intro">
      <h2>Our Partners</h2>
      <p>Impressive list of partners, working together, building solutions to drive business</p>
    </div>
    <div class="partner-logos">
      <span class="logo-name" style="left:0;top:10px"><span class="logo-sq"></span>Tradelink Mesh</span>
      <span class="logo-name" style="left:245px;top:10px">Brightfold Group</span>
      <span class="logo-name" style="left:530px;top:0"><span class="logo-sq"></span>Corvanta</span>
      <span class="logo-name" style="left:0;top:158px"><span class="logo-dot"></span>Pacemetric</span>
      <span class="logo-name" style="left:245px;top:135px"><span class="logo-dot"></span>Spanwire Business</span>
      <span class="logo-name" style="left:530px;top:95px">Linknetic</span>
      <span class="logo-name" style="left:530px;top:172px"><span class="logo-dot"></span>Altura Network</span>
    </div>
  </div>
</section>

<section class="team">
  <div class="wrap">
    <h2 class="section-title">Our Team of Experts</h2>
    <div class="team-cards">
      <div class="member">
        <svg class="member-photo" role="img" aria-label="Portrait photo of Tom Ashcroft, Director"><rect width="168" height="160" fill="#c9c3b8"/></svg>
        <h3>Tom Ashcroft</h3><div class="role">-Director-</div>
        <div class="profile"><span class="circle-link"></span>View Profile</div>
      </div>
      <div class="member">
        <svg class="member-photo" role="img" aria-label="Portrait photo of Daniel Verrier, Director"><rect width="168" height="160" fill="#b9a894"/></svg>
        <h3>Daniel Verrier</h3><div class="role">-Director-</div>
        <div class="profile"><span class="circle-link"></span>View Profile</div>
      </div>
      <div class="member">
        <svg class="member-photo" role="img" aria-label="Portrait photo of Peter Holloway, New Business Director"><rect width="168" height="160" fill="#4f8a6e"/></svg>
        <h3>Peter Holloway</h3><div class="role">-New Business Director-</div>
        <div class="profile"><span class="circle-link"></span>View Profile</div>
      </div>
      <div class="member">
        <svg class="member-photo" role="img" aria-label="Portrait photo of Helen Markby, Non-Executive Director"><rect width="168" height="160" fill="#6d6660"/></svg>
        <h3>Helen Markby</h3><div class="role">-Non-Executive Director-</div>
        <div class="profile"><span class="circle-link"></span>View Profile</div>
      </div>
    </div>
  </div>
</section>

<section class="clients">
  <div class="wrap">
    <div class="side-intro">
      <h2>Our Clients</h2>
      <p>You will find an impressive list of clients that QTA have worked with.</p>
    </div>
    <div class="client-logos">
      <span class="logo-name" style="left:290px;top:78px"><span class="logo-sq"></span>Tellrun</span>
      <span class="logo-name" style="left:540px;top:78px">Brightfold Group</span>
      <span class="logo-name" style="left:790px;top:72px">Portgate Labs</span>
      <span class="logo-name" style="left:0;top:228px"><span class="logo-sq"></span>Datalane</span>
      <span class="logo-name" style="left:290px;top:228px">Cellwave Memory</span>
      <span class="logo-name" style="left:540px;top:228px"><span class="logo-sq"></span>Tradelink Mesh</span>
      <span class="logo-name" style="left:790px;top:228px"><span class="logo-dot"></span>Harbourline Capital</span>
      <span class="logo-name" style="left:0;top:378px">Ardenfield Hosting</span>
      <span class="logo-name" style="left:290px;top:378px"><span class="logo-dot"></span>Joinpoint Systems</span>
      <span class="logo-name" style="left:540px;top:378px"><span class="logo-dot"></span>KVS Technology</span>
      <span class="logo-name" style="left:790px;top:378px"><span class="logo-dot"></span>Nexcrow</span>
    </div>
  </div>
</section>

<section class="info">
  <div class="wrap">
    <div class="case-studies">
      <h2>Quorvel Technology Advisers<br>– Case Studies –</h2>
      <ul class="case-list">
        <li><svg width="20" height="16" viewBox="0 0 20 16"><path d="M5 13a4 4 0 010-8 5 5 0 019-1 4 4 0 011 9z" fill="var(--red)"/><path d="M10 6v6M7.5 9.5L10 12l2.5-2.5" stroke="#fff" stroke-width="1.5" fill="none"/></svg>Infrastructure Case Study</li>
        <li><svg width="20" height="16" viewBox="0 0 20 16"><path d="M5 13a4 4 0 010-8 5 5 0 019-1 4 4 0 011 9z" fill="var(--red)"/><path d="M10 6v6M7.5 9.5L10 12l2.5-2.5" stroke="#fff" stroke-width="1.5" fill="none"/></svg>Tech-Startup-Case</li>
        <li><svg width="20" height="16" viewBox="0 0 20 16"><path d="M5 13a4 4 0 010-8 5 5 0 019-1 4 4 0 011 9z" fill="var(--red)"/><path d="M10 6v6M7.5 9.5L10 12l2.5-2.5" stroke="#fff" stroke-width="1.5" fill="none"/></svg>Tech-Due Diligence</li>
        <li><svg width="20" height="16" viewBox="0 0 20 16"><path d="M5 13a4 4 0 010-8 5 5 0 019-1 4 4 0 011 9z" fill="var(--red)"/><path d="M10 6v6M7.5 9.5L10 12l2.5-2.5" stroke="#fff" stroke-width="1.5" fill="none"/></svg>Training : Capital Markets Training</li>
        <li><svg width="20" height="16" viewBox="0 0 20 16"><path d="M5 13a4 4 0 010-8 5 5 0 019-1 4 4 0 011 9z" fill="var(--red)"/><path d="M10 6v6M7.5 9.5L10 12l2.5-2.5" stroke="#fff" stroke-width="1.5" fill="none"/></svg>Product development &amp; Technology Strategy</li>
      </ul>
    </div>
    <div class="about">
      <h2>About QTA</h2>
      <p>Since founding Quorvel Technology Advisers in 2014 we have dedicated ourselves to the provision of services. What differentiates us from other advisers or consultancies is a genuine motivation to see our clients succeed. Today's technology allows our clients to take their knowledge to the market in ways that previous generations could only dream of. That's why QTA is dedicated to seeing you choose the right technology strategy, ensuring you maintain a competitive edge over your peers.</p>
    </div>
  </div>
</section>

<footer>
  <div class="site-footer">
    <div class="wrap">
      <div class="footer-contact">
        <h4>Contact Details</h4>
        <div class="line"><svg width="13" height="10" viewBox="0 0 26 20"><rect x="1" y="1" width="24" height="18" fill="none" stroke="#d8d8d8" stroke-width="2"/><path d="M1 1l12 10L25 1" fill="none" stroke="#d8d8d8" stroke-width="2"/></svg>admin@quorvel-group.com</div>
        <p>Suite 4 Larchfield Court,<br>Brookmere, Aldwick,<br>Hants, AH12 6PL<br>Company No:08417263<br>VAT No: 518204</p>
      </div>
      <div class="footer-privacy">
        <h4>Privacy</h4>
        <p>QTA may receive names, e-mail addresses and other personally identifying information only when personally submitted by users through the optional QTA feedback feature. This information is not gathered by QTA without the user's knowledge, active permission and participation. The information submitted enables QTA to respond to user inquiries and suggestions. QTA respects the privacy of users visiting this Web site and does not sell any personally identifiable information to any third parties. If you would like to change or remove any information you have submitted to QTA, please contact Sales and Marketing by emailing sales@quorvel-group.com or calling +44(0)20 7946 0382.</p>
      </div>
    </div>
  </div>
  <nav class="footer-nav"><span>Home</span><span>What We Do</span><span>How We do it</span><span>Who Are We</span><span>Why use us?</span><span>Contact</span></nav>
  <div class="copyright">
    <div class="wrap"><span>Copyright © 2017 Quorvel Technology Advisers.</span><span>Social</span></div>
  </div>
</footer>

</body>
</html>
```